Wellness Thai Massage Geschäft benötigt eine Preis/Info Broschüre

Ein kleines Thai Massage Geschäft in Bayern: Sukonta Thaimassage
Benötigt eine kleine Preisliste, sowie eine kurze Beschreibung vom Unternehmen. Angeboten werden traditionelle Thaimassagen. Der Farbstil soll dem Logo (Anhang) angepasst sein. Alle Bilder außer die Bilder von der Geschäftsführerin sind optional zur Verwendung verfügbar. Mehr Info wie Preise, etc. sind verfügbar auf der Website https://www.sukontathaimassage-beispiel.de/

```html
<!DOCTYPE html>
<html lang="de">
<head>
<meta charset="utf-8">
<title>Sukonta Thaimassage – Broschüre</title>
<link rel="stylesheet" href="https://fonts.googleapis.com/css2?family=Roboto+Condensed:ital,wght@0,300;0,400;0,700;1,400;1,700&family=Great+Vibes&display=swap">
<style>
:root{
  --wine:#8a1a1f;
  --wine-dark:#6e1217;
  --rose:#e0284f;
  --pink:#e8456b;
  --cream:#fdf5c9;
  --cream-soft:#fbf1c8;
  --gold:#e8912a;
  --ink:#2b2b2b;
  --stage:#c4c4c4;
  --blush:#f6eceb;
}
*{box-sizing:border-box;margin:0;padding:0}
html,body{width:1018px;height:1200px;overflow:hidden}
body{background:var(--stage);font-family:"Roboto Condensed",Arial,sans-serif;color:var(--ink);position:relative}
.spread{position:absolute;width:678px;height:480px;display:flex;background:#fff}
.spread--cover{left:147px;top:91px}
.spread--inside{left:215px;top:645px}
.panel{position:relative;width:339px;height:480px;overflow:hidden}
.photo{position:absolute}
.wave{position:absolute;left:0;bottom:0;width:339px}
.site{position:absolute;left:0;width:339px;text-align:center;color:#fff;font-size:14px;font-weight:300;bottom:10px}
.site b{font-weight:700}

/* brand name */
.brand{position:absolute;display:flex;align-items:center;gap:8px}
.brand .dot{width:26px;height:26px;border-radius:50%;background:var(--cream);flex:none}
.brand .name{color:var(--wine);font-weight:700;font-size:17px;line-height:20px;white-space:nowrap}

/* contact panel */
.contact{background:var(--cream)}
.contact .room{left:0;top:0;width:339px;height:200px;background:linear-gradient(160deg,#a9373a 0%,#7a2025 45%,#c9b7a8 100%)}
.contact .top-curve{position:absolute;left:0;top:150px;width:339px}
.contact .statue{left:139px;top:123px;width:88px;height:88px;border-radius:50%;border:3px solid #fff;background:radial-gradient(circle at 50% 45%,#6a5a4a,#3c2f28 60%,#9d3b3b)}
.script-title{position:absolute;width:339px;text-align:center;font-family:"Great Vibes",cursive;color:var(--wine);font-size:34px;top:214px;left:-4px}
.kontakt-sub{position:absolute;top:247px;width:339px;text-align:center;color:var(--wine);font-style:italic;font-weight:700;font-size:13px}
.address{position:absolute;right:185px;top:273px;text-align:right;color:var(--wine-dark);font-size:12px;line-height:15px}
.address .tel{font-size:18px;font-weight:700;color:var(--wine);line-height:24px}
.address .mail{font-size:10px;font-weight:300;color:var(--wine)}
.divider{position:absolute;left:168px;top:275px;width:1px;height:60px;background:var(--wine)}
.hours{position:absolute;left:182px;top:275px;color:var(--wine);font-size:10px;line-height:12.8px;font-weight:300}
.hours h3{font-size:10px;font-weight:700;letter-spacing:.2px}
.booking{position:absolute;top:345px;width:339px;text-align:center;color:var(--wine)}
.booking h3{font-size:10px;font-weight:700}
.booking p{font-size:10px;font-style:italic;line-height:13px;font-weight:300}

/* welcome panel */
.welcome{background:linear-gradient(180deg,#fff 70%,#ececec 88%)}
.welcome .model{left:0;top:0;width:339px;height:325px;background:linear-gradient(135deg,#f3e3dc 0%,#e9c9b8 40%,#f5efec 75%,#fbfbfb 100%)}
.welcome .brand{left:150px;top:31px}
.badge{position:absolute;left:184px;top:224px;width:120px;height:120px;border-radius:50%;background:radial-gradient(circle at 40% 35%,#f26483,var(--rose));color:#fff;text-align:center;font-size:9.5px;font-style:italic;line-height:11.5px;padding-top:20px}
.badge b{font-weight:700}
.call{position:absolute;left:176px;top:307px;width:128px;height:23px;border-radius:12px;background:var(--wine);color:#fff;font-weight:700;font-size:17px;display:flex;align-items:center;gap:3px;padding-left:3px;box-shadow:0 1px 3px rgba(0,0,0,.3)}
.call svg{flex:none}
.welcome-title{position:absolute;top:326px;width:339px;text-align:center;font-family:"Great Vibes",cursive;color:var(--wine);font-size:62px;line-height:70px}
.welcome-sub{position:absolute;top:388px;width:339px;text-align:center;color:var(--rose);font-size:16px;font-weight:300;letter-spacing:.5px}

/* inside left */
.about{background:linear-gradient(180deg,#fff 0%,var(--blush) 100%)}
.about .studio{left:23px;top:20px;width:96px;height:219px;background:linear-gradient(180deg,#e7c56a 0%,#c58a3a 40%,#a24a3e 65%,#efe6de 100%)}
.copy{position:absolute;left:129px;width:188px}
.copy h2{font-size:12px;font-weight:700;color:var(--wine);background:linear-gradient(90deg,var(--cream) 0%,#fff6d6 100%);display:flex;align-items:center;gap:4px;height:14px;margin-bottom:3px}
.copy h2 .bullet{width:10px;height:10px;border-radius:50%;background:#e89ac7;margin-left:2px}
.copy p{font-size:8.2px;line-height:10.6px;text-align:justify;font-weight:400;color:#333}
.copy--what{top:19px}
.copy--us{top:117px}
.prices{position:absolute;left:23px;top:250px;width:295px;border-collapse:collapse;font-size:9px}
.prices th{background:var(--wine);color:#fff;font-weight:700;text-align:left;height:23px;padding-left:11px;font-size:9.5px}
.prices th.c{text-align:center;padding:0}
.prices td{background:var(--cream-soft);border:1px solid var(--wine);color:var(--wine);height:34px;font-weight:300;line-height:10px}
.prices td.svc{font-weight:700;padding-left:9px;width:152px}
.prices td.min{padding-left:14px;width:72px}
.prices td.eur{background:var(--wine);color:#fff;padding-left:18px}
.prices tr.short td{height:24px}

/* inside right */
.offers{background:linear-gradient(180deg,#fff 0%,#fbf7f4 100%)}
.offer{position:absolute;left:20px;width:300px;display:flex;gap:12px}
.offer .thumb{width:72px;height:55px;flex:none}
.offer .body{width:216px}
.offer h3{font-size:11.5px;font-weight:700;color:var(--wine);border-bottom:1px solid #d9a0a0;line-height:13px;padding-bottom:1px;margin-bottom:2px}
.offer p{font-size:7.8px;line-height:10px;text-align:justify;color:#444}
.note{position:absolute;top:352px;left:20px;width:300px;text-align:center;font-size:7.8px;line-height:10px;font-style:italic;color:#555}
.note b{display:block;color:var(--wine);margin-top:7px}
.offers .brand{left:82px;top:408px}
</style>
</head>
<body>

<section class="spread spread--cover">
  <div class="panel contact">
    <div class="photo room" role="img" aria-label="Foto: Behandlungsraum mit Massageliegen und roten Wänden"></div>
    <svg class="top-curve" width="339" height="60" viewBox="0 0 339 60">
      <path d="M0 40 Q150 0 339 20 L339 60 L0 60Z" fill="var(--cream)"/>
      <path d="M0 40 Q150 0 339 20 L339 28 Q150 8 0 48Z" fill="var(--wine)"/>
      <path d="M0 48 Q150 8 339 28 L339 31 Q150 12 0 51Z" fill="var(--rose)"/>
    </svg>
    <div class="photo statue" role="img" aria-label="Foto: Buddha-Figur mit Blüten"></div>
    <div class="script-title">Kontakt:</div>
    <div class="kontakt-sub">Bei Fragen &amp; anderen Kontaktgründen</div>
    <div class="address">
      Lindenweg 14<br>Musterstadt 83000
      <div class="tel">0170 1234567</div>
      <div class="mail">info@sukonta-beispiel.de</div>
    </div>
    <div class="divider"></div>
    <div class="hours">
      <h3>ÖFFNUNGSZEITEN:</h3>
      Montag: 9.00 - 20.00 Uhr<br>
      Dienstag - Freitag: 10.00 - 20.00 Uhr<br>
      Samstag: 10.00 - 18.00 Uhr<br>
      Sonntag: Ruhetag
    </div>
    <div class="booking">
      <h3>TERMINVEREINBARUNG</h3>
      <p>Damit wir uns die Zeit nehmen können, bitten wir sie ihren<br>Termin im Vorfeld telefonisch mit uns zu vereinbaren</p>
    </div>
    <svg class="wave" width="339" height="62" viewBox="0 0 339 62">
      <path d="M0 18 Q170 -2 339 8 L339 62 L0 62Z" fill="var(--rose)"/>
      <path d="M0 28 Q170 8 339 16 L339 62 L0 62Z" fill="var(--wine)"/>
    </svg>
    <div class="site">www.<b>SukontaThaimassage</b>-beispiel.de</div>
  </div>

  <div class="panel welcome">
    <div class="photo model" role="img" aria-label="Foto: entspannte Frau bei einer Rückenmassage"></div>
    <div class="brand">
      <span class="dot"></span>
      <span class="name">Sukonta Thaimassage</span>
    </div>
    <div class="badge">Buchen sie<br>Termine entweder<br>per Whatsapp, Anruf<br>oder direkt vor Ort.<br><b>Vielen Dank!</b></div>
    <div class="call">
      <svg width="18" height="18" viewBox="0 0 18 18"><circle cx="9" cy="9" r="9" fill="#fff"/><path d="M6 4.5l1.8 0 .8 2.3-1.2.9c.6 1.3 1.6 2.3 2.9 2.9l.9-1.2 2.3.8 0 1.8c0 .5-.4.9-.9.9C8.5 12.7 5.1 9.3 5.1 5.4c0-.5.4-.9.9-.9z" fill="var(--wine)"/></svg>
      0170 1234567
    </div>
    <div class="welcome-title">Willkommen</div>
    <div class="welcome-sub">SUKONTA THAIMASSAGE</div>
    <svg class="wave" width="339" height="82" viewBox="0 0 339 82">
      <path d="M0 40 Q200 30 339 0 L339 82 L0 82Z" fill="var(--gold)"/>
      <path d="M0 40 Q200 34 339 8 L339 82 L0 82Z" fill="var(--cream)"/>
      <path d="M0 42 Q200 40 339 14 L339 82 L0 82Z" fill="var(--rose)"/>
      <path d="M0 46 Q200 46 339 20 L339 82 L0 82Z" fill="var(--wine)"/>
    </svg>
    <div class="site">www.<b>SukontaThaimassage</b>-beispiel.de</div>
  </div>
</section>

<section class="spread spread--inside">
  <div class="panel about">
    <div class="photo studio" role="img" aria-label="Foto: Masseurin bei einer traditionellen Thai-Massage im Studio"></div>
    <div class="copy copy--what">
      <h2><span class="bullet"></span>Was ist Thai Massage eigentlich?</h2>
      <p>Thai Massage existiert schon seit ca. über 2500 Jahren welches sich im Laufe der Zeit zu einer effektiven Methode gegen Schmerzzustände und auch Krankheiten entwickelt welches in der heutigen Zeit sogar Kultstatus erreicht hat. Diese thailändische Heilungsmethode verlangt eine professionelle Ausbildung die Hintergrundwissen und langes Training mit sich bringt.</p>
    </div>
    <div class="copy copy--us">
      <h2><span class="bullet"></span>Über uns</h2>
      <p>Sukonta Thaimassage legt einen hohen Wert auf die Zufriedenheit und das Wohlbefinden von jedem Kunden. Wenn sie also z.B nach viel Arbeit gestresst sind und Schmerzen an einer bestimmten Region aufgebaut haben, dann sind sie bei uns an der richtigen Adresse. Geführt wird das Massagestudio von Malee Hofbauer, die professionell ausgebildet wurde und auch beruflich schon in Deutschland sowie in Thailand viel Erfahrung gesammelt hat. Wir freuen uns schon auf ihren Besuch bei Sukonta Thaimassage!</p>
    </div>
    <table class="prices">
      <tr><th>PRICE LIST</th><th class="c">MINUTEN</th><th class="c">EURO</th></tr>
      <tr><td class="svc">Traditionelle Thai-Sport Massage</td><td class="min">60 Minuten<br>90 Minuten</td><td class="eur">54 Euro<br>76 Euro</td></tr>
      <tr><td class="svc">Aromaöl Massage</td><td class="min">60 Minuten<br>90 Minuten</td><td class="eur">51 Euro<br>72 Euro</td></tr>
      <tr class="short"><td class="svc">Hot Stone Massage</td><td class="min">90 Minuten</td><td class="eur">83 Euro</td></tr>
      <tr><td class="svc">Fussreflexzonen Massage</td><td class="min">30 Minuten<br>60 Minuten</td><td class="eur">35 Euro<br>62 Euro</td></tr>
      <tr><td class="svc">Rücken-Thai Massage</td><td class="min">30 Minuten<br>60 Minuten</td><td class="eur">35 Euro<br>72 Euro</td></tr>
    </table>
    <svg class="wave" width="339" height="30" viewBox="0 0 339 30">
      <path d="M0 18 Q170 0 339 12 L339 30 L0 30Z" fill="var(--rose)"/>
      <path d="M0 24 Q170 8 339 16 L339 30 L0 30Z" fill="var(--wine)"/>
    </svg>
  </div>

  <div class="panel offers">
    <div class="offer" style="top:16px">
      <div class="thumb" role="img" aria-label="Foto: Thai-Sport Massage im Sitzen" style="background:linear-gradient(135deg,#8a6f7a,#b2243a 55%,#e8e4ea)"></div>
      <div class="body" style="padding-top:2px"><h3>Traditionelle Thai-Sport Massage</h3>
      <p>Mt der traditionellen Thai-Massage werden durch Akupressur, Dehnung und Energielinien-Massage Energieblockaden gelöst. Es wird an 10 Energiepunkten und Linien massiert, die für den Einklang von Körper und Geist wichtig sind. Somit wird eine innere Balance und der Fluss der Lebensenergie erreicht</p></div>
    </div>
    <div class="offer" style="top:79px">
      <div class="thumb" role="img" aria-label="Foto: Kerzen und Aromaöle" style="background:linear-gradient(135deg,#5a6a5a,#c23a4a 50%,#9a8ac0)"></div>
      <div class="body" style="padding-top:15px"><h3>Aromaöl Massage</h3>
      <p>Die Aromaöl Massage ist eine Behandlungsform zur Regeneration und Harmonisierung des gesamten Körpers. Dabei wird das Basisöl mit ätherischen Ölen angereichert. Die Aromatherapie kann anregend oder entspannend abgestimmt werden</p></div>
    </div>
    <div class="offer" style="top:143px">
      <div class="thumb" role="img" aria-label="Foto: heiße Steine mit Blüten" style="background:radial-gradient(circle at 50% 55%,#2a2a2a,#4a4048 50%,#a04070)"></div>
      <div class="body" style="padding-top:16px"><h3>Hot Stone Massage</h3>
      <p>Die Aromaöl Massage ist eine Behandlungsform zur Regeneration und Harmonisierung des gesamten Körpers. Dabei wird das Basisöl mit ätherischen Ölen angereichert. Die Aromatherapie kann anregend oder entspannend abgestimmt werden</p></div>
    </div>
    <div class="offer" style="top:206px">
      <div class="thumb" role="img" aria-label="Foto: Fussreflexzonen-Behandlung" style="background:linear-gradient(135deg,#d9b24a,#a8553a 55%,#e8dcd0)"></div>
      <div class="body" style="padding-top:20px"><h3>Fussreflexzonen Massage</h3>
      <p>Eine Massage für den wohl für den strapaziertesten Körperteil, den Füssen, setzt neue Kräfte frei und verleiht Vitalität</p></div>
    </div>
    <div class="offer" style="top:271px">
      <div class="thumb" role="img" aria-label="Foto: Rückenmassage mit Dehnung" style="background:linear-gradient(135deg,#e0b84a,#9a3a40 50%,#c8c0c8)"></div>
      <div class="body" style="padding-top:3px"><h3>Rücken-Thai Massage</h3>
      <p>Bei dieser Massagetechnik wird größtenteils der Rücken sowie auch Nacken, Hinterkopf, Schulter und Finger involviert. Diese Massage eignet sich besonders falls eines dieser Bereiche verspannt oder Schmerzen verursacht.</p></div>
    </div>
    <div class="note">Infos über weitere Angebote werden hier in Zukunft noch eingefügt. Bitte erkundigen sie<br>sich hierfür im Geschäft um über ein erweitertes Angebot zu erfahren.<b>Traditional Thai massages are offered.</b></div>
    <div class="brand">
      <span class="dot"></span>
      <span class="name">Sukonta Thaimassage</span>
    </div>
    <svg class="wave" width="339" height="50" viewBox="0 0 339 50">
      <path d="M0 40 Q200 30 339 0 L339 50 L0 50Z" fill="var(--gold)"/>
      <path d="M0 40 Q200 33 339 7 L339 50 L0 50Z" fill="var(--cream)"/>
      <path d="M0 41 Q200 38 339 12 L339 50 L0 50Z" fill="var(--rose)"/>
      <path d="M0 44 Q200 44 339 18 L339 50 L0 50Z" fill="var(--wine)"/>
    </svg>
  </div>
</section>

</body>
</html>
```